Playful Website Design Needed Pet Sitting and Dog Walking Business

Need a simple one page Web Design Built on WordPress.
Sections:

About Us
Services Provided
Costs
Contact Us
Intake Form (Questionnaire that goes to email)
See us in Action

Industry/Entity Type

Pet Sitting and Dog Walking

Number of Pages Required

1 page

Font styles to use
Other font styles liked:
• See the Business Card Font and use that.

Colors
EE7325
F08F49
F5BC92
FAE3D3
FDF4ED

Requirements
Must have
• See attached Logo Design, with Font's and Colors Use these as theme guide

```html
<!DOCTYPE html>
<html lang="en">
<head>
<meta charset="utf-8">
<title>Paws &amp; Play Sitters</title>
<link href="https://fonts.googleapis.com/css2?family=Patrick+Hand&family=Poppins:wght@300;400;500;600&display=swap" rel="stylesheet">
<style>
:root{
  --orange:#EE7325;
  --orange-2:#F08F49;
  --peach:#F5BC92;
  --cream:#FAE3D3;
  --shell:#FDF4ED;
  --ink:#3b3431;
  --muted:#7b6f69;
  --white:#ffffff;
  --green:#4e9a3a;
}
*{box-sizing:border-box;margin:0;padding:0}
html,body{width:1200px;height:3104px;overflow:hidden}
body{font-family:"Poppins",sans-serif;color:var(--ink);background:var(--white);font-size:14px;position:relative}
.section{position:absolute;left:0;width:1200px}

/* header */
.site-header{top:0;height:88px;display:flex;align-items:center;padding:0 200px 0 220px;justify-content:space-between;z-index:3}
.brand{display:flex;align-items:center;gap:10px;font-family:"Patrick Hand",cursive;font-size:26px;color:var(--orange);line-height:1}
.brand-dot{width:22px;height:22px;border-radius:50%;background:var(--orange)}
.nav{display:flex;gap:56px;align-items:center;font-size:14px}
.nav a{color:var(--ink);text-decoration:none}
.btn{display:inline-block;background:var(--orange);color:var(--white);font-size:13px;padding:7px 22px;text-decoration:none;border-radius:2px}
.nav a.btn{color:var(--white)}

/* hero */
.hero{top:0;height:560px;background:linear-gradient(180deg,#f6efe9 0%,#f9f3ee 100%);overflow:hidden}
.hero-bg{position:absolute;left:0;top:0;width:700px;height:560px;background:linear-gradient(160deg,#e9dcd2,#f6ede6);opacity:.8}
.hero-blob{position:absolute;right:0;top:0;width:520px;height:560px}
.hero-pets{position:absolute;left:760px;top:120px;width:300px;height:320px;border-radius:48% 52% 18% 22% / 40% 42% 12% 14%;background:linear-gradient(160deg,#8d7a68 0%,#b59d82 45%,#d9c6ae 100%)}
.hero-copy{position:absolute;left:200px;top:210px}
.hero-title{font-family:"Patrick Hand",cursive;font-size:56px;line-height:1.05;color:var(--orange);font-weight:400}
.hero-title .accent{color:var(--orange-2)}
.hero-copy .btn{margin-top:26px}

/* welcome */
.welcome{top:600px;height:430px}
.welcome-copy{position:absolute;left:200px;top:40px;width:390px}
.welcome-title{font-family:"Patrick Hand",cursive;font-size:38px;line-height:1.05;color:var(--orange-2);font-weight:400}
.welcome-title span{color:var(--orange)}
.welcome-copy p{margin-top:16px;font-size:12px;line-height:1.9;color:var(--muted)}
.welcome-photo{position:absolute;left:620px;top:20px;width:280px;height:280px;border-radius:50%;background:linear-gradient(135deg,#6c8b3d,#b9c07a)}
.welcome-dog{position:absolute;left:40px;top:240px;width:150px;height:110px;border-radius:50% 40% 40% 50%;background:linear-gradient(135deg,#f1d6bf,#e5a06b)}

/* services */
.services{top:1060px;height:270px;background:var(--shell)}
.section-title{font-family:"Patrick Hand",cursive;font-size:38px;color:var(--green);text-align:center;font-weight:400}
.services .section-title{margin-top:36px}
.service-list{display:flex;justify-content:center;gap:120px;margin-top:28px}
.service{width:220px;text-align:center;font-size:13px;color:var(--green)}
.service svg{width:54px;height:54px;display:block;margin:0 auto 12px}

/* costs */
.costs{top:1340px;height:500px}
.costs .section-title{margin-top:24px;color:var(--orange)}
.plans{position:absolute;left:200px;top:100px;width:800px;display:flex;justify-content:space-between;align-items:flex-start}
.plan{width:240px;background:var(--white);box-shadow:0 4px 18px rgba(0,0,0,.08);padding:16px 18px 18px;text-align:center}
.plan.featured{background:var(--shell);margin-top:-22px;padding-top:28px;padding-bottom:26px}
.plan-name{font-family:"Patrick Hand",cursive;font-size:28px;color:var(--green);line-height:1.2}
.plan-price{font-family:"Patrick Hand",cursive;font-size:20px;color:var(--orange);margin-bottom:8px}
.plan ul{list-style:none;font-size:11px;color:var(--muted)}
.plan li{padding:6px 0;border-bottom:1px solid var(--cream)}
.plan .btn{margin-top:12px;font-size:11px;padding:5px 16px}
.plan-icon{width:40px;height:40px;margin:0 auto 4px;display:block}

/* dog strip */
.dog-strip{top:1860px;height:165px;display:flex;justify-content:space-between;padding:0 40px;align-items:flex-end}
.dog{width:150px;height:160px;border-radius:45% 45% 10% 10%}

/* gallery */
.gallery{top:2030px;height:500px;background:var(--shell)}
.gallery .section-title{margin-top:20px}
.gallery-grid{position:absolute;left:192px;top:90px;width:816px;display:grid;grid-template-columns:repeat(4,1fr);gap:16px}
.photo{height:190px}

/* enquiry */
.enquiry{top:2560px;height:330px}
.enquiry .section-title{margin-top:6px}
.enquiry-form{position:absolute;left:232px;top:64px;width:736px;height:250px;background:var(--shell);box-shadow:0 4px 18px rgba(0,0,0,.06);padding:22px 44px}
.form-row{display:flex;gap:20px;margin-bottom:12px}
.field{flex:1;height:30px;background:var(--white);border:1px solid var(--cream);font-size:11px;color:var(--muted);padding:7px 10px}
.field.message{height:76px}
.enquiry-form .btn{display:block;width:130px;margin:2px auto 0;text-align:center;font-size:12px}

/* footer */
.site-footer{top:2900px;height:204px;background:var(--cream)}
.footer-col{position:absolute;top:26px;font-size:12px;color:var(--muted);line-height:2}
.footer-col h3{font-family:"Patrick Hand",cursive;font-size:24px;color:var(--green);font-weight:400;line-height:1.2;margin-bottom:6px}
.footer-contact{left:230px}
.footer-contact .row{display:flex;align-items:center;gap:8px}
.footer-contact svg{width:13px;height:13px;fill:var(--orange)}
.footer-brand{left:0;width:1200px;text-align:center;top:40px}
.footer-brand .brand{justify-content:center;font-size:28px}
.socials{display:flex;justify-content:center;gap:8px;margin-top:20px}
.socials span{width:24px;height:24px;background:var(--orange)}
.footer-hours{right:230px;text-align:right}
.footer-hours b{color:var(--ink);font-weight:500}
.footer-hours em{color:var(--orange);font-style:normal}
.copyright{position:absolute;bottom:12px;width:100%;text-align:center;font-size:10px;color:var(--muted)}
</style>
</head>
<body>

<section class="section hero">
  <div class="hero-bg" role="img" aria-label="Faded photo of a person walking several dogs"></div>
  <svg class="hero-blob" viewBox="0 0 520 560" preserveAspectRatio="none" aria-hidden="true"><path d="M40 0 L520 0 L520 430 C470 500 380 560 280 540 C190 520 150 460 160 390 C170 320 60 300 20 220 C-10 150 10 60 40 0Z" fill="#F08F49"/></svg>
  <div class="hero-pets" role="img" aria-label="Photo of a cat and a dog sitting together"></div>
  <div class="hero-copy">
    <h1 class="hero-title">We Feed, Walk and<br>Play with Your Pet,<br><span class="accent">Each Visit!</span></h1>
    <a class="btn" href="#enquiry">Contact Us</a>
  </div>
</section>

<header class="section site-header">
  <div class="brand"><span class="brand-dot"></span>Paws &amp; Play Sitters</div>
  <nav class="nav">
    <a href="#">Home</a><a href="#">Services</a><a href="#">Team</a><a href="#">Gallery</a>
    <a class="btn" href="#enquiry">Contact Us</a>
  </nav>
</header>

<section class="section welcome">
  <div class="welcome-copy">
    <h2 class="welcome-title">Welcome<br><span>Paws &amp; Play Sitters</span></h2>
    <p>We are a small, friendly team of pet lovers who care for your animals as if they were our own. From daily walks to feeding visits and playtime, we keep your pets happy, safe and loved while you are away. Every visit is tailored to your pet's routine, and you get an update after each one so you never have to wonder how they are doing.</p>
  </div>
  <div class="welcome-photo" role="img" aria-label="Photo of a sitter sitting on grass with a golden dog"></div>
  <div class="welcome-dog" role="img" aria-label="Illustration of a running puppy"></div>
</section>

<section class="section services">
  <h2 class="section-title">Our Services</h2>
  <div class="service-list">
    <div class="service">
      <svg viewBox="0 0 54 54" fill="none" stroke="#4e9a3a" stroke-width="2"><rect x="8" y="12" width="38" height="34" rx="3"/><path d="M8 22h38M18 8v8M36 8v8"/><path d="M20 33l5 5 10-10"/></svg>
      All year round &amp; 7 days a week
    </div>
    <div class="service">
      <svg viewBox="0 0 54 54" fill="none" stroke="#4e9a3a" stroke-width="2"><circle cx="27" cy="34" r="9"/><circle cx="14" cy="20" r="4"/><circle cx="22" cy="12" r="4"/><circle cx="32" cy="12" r="4"/><circle cx="40" cy="20" r="4"/></svg>
      All pets, any age
    </div>
    <div class="service">
      <svg viewBox="0 0 54 54" fill="none" stroke="#4e9a3a" stroke-width="2"><path d="M27 6l17 7v12c0 11-8 19-17 23C18 44 10 36 10 25V13z"/><path d="M19 27l6 6 11-11"/></svg>
      Always supervised
    </div>
  </div>
</section>

<section class="section costs">
  <h2 class="section-title">Costs</h2>
  <div class="plans">
    <div class="plan">
      <svg class="plan-icon" viewBox="0 0 40 40" fill="none" stroke="#EE7325" stroke-width="2"><path d="M6 36V18l14-10 14 10v18z"/><path d="M15 36V26h10v10"/></svg>
      <div class="plan-name">Puppy School</div>
      <div class="plan-price">$25/session</div>
      <ul><li>Obedience training</li><li>Group classes</li><li>Certified professional dog trainer</li><li>Socialization class</li><li>Treats as rewards for good behaviour</li></ul>
      <a class="btn" href="#">Contact Us</a>
    </div>
    <div class="plan featured">
      <svg class="plan-icon" viewBox="0 0 40 40" fill="none" stroke="#EE7325" stroke-width="2"><circle cx="20" cy="24" r="8"/><circle cx="9" cy="13" r="3"/><circle cx="16" cy="7" r="3"/><circle cx="24" cy="7" r="3"/><circle cx="31" cy="13" r="3"/></svg>
      <div class="plan-name">Obedience Class</div>
      <div class="plan-price">$30/session</div>
      <ul><li>Obedience training</li><li>Group classes</li><li>Certified professional dog trainer</li><li>Socialization class</li><li>Treats as rewards for good behaviour</li></ul>
      <a class="btn" href="#">Contact Us</a>
    </div>
    <div class="plan">
      <svg class="plan-icon" viewBox="0 0 40 40" fill="none" stroke="#EE7325" stroke-width="2"><path d="M4 34h32M8 34V18M32 34V18M8 22h24"/></svg>
      <div class="plan-name">Agility Course</div>
      <div class="plan-price">$35/session</div>
      <ul><li>Obedience training</li><li>Group classes</li><li>Certified professional dog trainer</li><li>Socialization class</li><li>Treats as rewards for good behaviour</li></ul>
      <a class="btn" href="#">Contact Us</a>
    </div>
  </div>
</section>

<section class="section dog-strip">
  <div class="dog" style="background:linear-gradient(180deg,#3a2a20,#1c1410)" role="img" aria-label="Photo of a black labrador"></div>
  <div class="dog" style="background:linear-gradient(180deg,#c98a50,#f2e6d8)" role="img" aria-label="Photo of a beagle"></div>
  <div class="dog" style="background:linear-gradient(180deg,#f4f1ee,#ddd6d0)" role="img" aria-label="Photo of a small white dog"></div>
  <div class="dog" style="background:linear-gradient(180deg,#b06c34,#6b3e1e)" role="img" aria-label="Photo of a boxer"></div>
  <div class="dog" style="background:linear-gradient(180deg,#e2b46e,#c18a48)" role="img" aria-label="Photo of a golden retriever"></div>
  <div class="dog" style="background:linear-gradient(180deg,#2b2420,#8a6140)" role="img" aria-label="Photo of a rottweiler"></div>
</section>

<section class="section gallery">
  <h2 class="section-title">Photo Gallery</h2>
  <div class="gallery-grid">
    <div class="photo" style="background:linear-gradient(135deg,#555,#999)" role="img" aria-label="Black and white photo of a dog walker with dogs"></div>
    <div class="photo" style="background:linear-gradient(135deg,#6c8b3d,#c9b48a)" role="img" aria-label="Photo of a sitter hugging a dog on grass"></div>
    <div class="photo" style="background:linear-gradient(135deg,#888,#ccc)" role="img" aria-label="Black and white photo of a cat and a dog"></div>
    <div class="photo" style="background:linear-gradient(135deg,#5d7a3a,#a9b889)" role="img" aria-label="Photo of a dog playing outdoors"></div>
    <div class="photo" style="background:linear-gradient(135deg,#7a5b3c,#d8b48a)" role="img" aria-label="Photo of a puppy and a kitten"></div>
    <div class="photo" style="background:linear-gradient(135deg,#666,#aaa)" role="img" aria-label="Black and white photo of a dog"></div>
    <div class="photo" style="background:linear-gradient(135deg,#a9774a,#e0c39f)" role="img" aria-label="Photo of a dog resting"></div>
    <div class="photo" style="background:linear-gradient(135deg,#777,#bbb)" role="img" aria-label="Black and white photo of a sleeping cat"></div>
  </div>
</section>

<section class="section enquiry" id="enquiry">
  <h2 class="section-title">Enquire Now!</h2>
  <form class="enquiry-form">
    <div class="form-row"><div class="field">First Name</div><div class="field">Last Name</div></div>
    <div class="form-row"><div class="field">Phone</div><div class="field">Select Your Pet</div></div>
    <div class="form-row"><div class="field message">Message</div></div>
    <a class="btn" href="#">Submit Now</a>
  </form>
</section>

<footer class="section site-footer">
  <div class="footer-col footer-contact">
    <h3>Connect Me</h3>
    <div class="row"><svg viewBox="0 0 24 24"><path d="M6 2l4 4-2 3c1 3 4 6 7 7l3-2 4 4-3 4C10 22 2 14 2 5z"/></svg>+1 (555) 014-2290</div>
    <div class="row"><svg viewBox="0 0 24 24"><path d="M2 5h20v14H2zm2 2v.5l8 5 8-5V7z"/></svg>hello@pawsplaysitters.com</div>
    <div class="row"><svg viewBox="0 0 24 24"><path d="M12 2a7 7 0 0 1 7 7c0 5-7 13-7 13S5 14 5 9a7 7 0 0 1 7-7zm0 4a3 3 0 1 0 0 6 3 3 0 0 0 0-6z"/></svg>18 Maple Lane, Brookfield</div>
  </div>
  <div class="footer-col footer-brand">
    <div class="brand"><span class="brand-dot"></span>Paws &amp; Play Sitters</div>
    <div class="socials"><span></span><span></span><span></span></div>
  </div>
  <div class="footer-col footer-hours">
    <h3>Working Hours</h3>
    <div><b>Mon - Fri:</b> <em>7am - 7pm</em></div>
    <div><b>Saturday:</b> <em>8am - 5pm</em></div>
    <div><b>Sunday:</b> <em>Closed</em></div>
  </div>
  <div class="copyright">Copyright 2024 Paws &amp; Play Sitters. All Rights Reserved.</div>
</footer>

</body>
</html>
```